Quarvelon stickers design for our main topics (for example: agile and Kanban)

We are looking for sticker design, that will reflect our cooperate identity and can be used for the different topics in our company. We would like to start with our Agile Coaching Offers with a Kanban Sticker saying "stop starting, start finishing", A bad example can be find in the file upload ;)
Check out our homepage to get a feeling for the cooperate identity (www.quarvelon-beispiel.ch)

Target Market(s)

Customers and trainees from our trainings

Industry/Entity Type

Consulting

Colors
0355a3
fbed22

Requirements
Must have
• a cool design thats fits to our customer design
the 2 lines can be changed for future stickers ... like in the example "stop starting, start finishing" and "we show you how"
Nice to have
• -
Should not have
• -

```html
<!DOCTYPE html>
<html lang="en">
<head>
<meta charset="utf-8">
<title>Quarvelon Kanban Sticker</title>
<link rel="stylesheet" href="https://fonts.googleapis.com/css2?family=Kalam:wght@400;700&display=swap">
<style>
  :root {
    --sticker-bg: #f9f9fc;
    --frame: #000000;
    --brand-blue: #0b47f7;
    --brand-yellow: #f2f21a;
    --ink: #000000;
  }
  html, body {
    margin: 0;
    padding: 0;
    width: 1200px;
    height: 432px;
    overflow: hidden;
    background: #ffffff;
  }
  .sticker {
    display: block;
    width: 1200px;
    height: 432px;
  }
  .sticker-text {
    font-family: "Kalam", "Comic Sans MS", cursive;
    font-weight: 700;
  }
  .headline { fill: var(--brand-yellow); font-size: 76px; }
  .tagline { fill: var(--ink); font-size: 104px; }
  .web-address { fill: var(--ink); font-size: 52px; }
  .company-name { fill: var(--ink); font-size: 34px; font-weight: 400; }
</style>
</head>
<body>
<svg class="sticker" viewBox="0 0 1200 432" xmlns="http://www.w3.org/2000/svg" aria-labelledby="sticker-title">
  <title id="sticker-title">Stop starting, Start finishing – We show you how – Quarvelon ag</title>

  <rect class="sticker-frame" x="4" y="4" width="1192" height="424" rx="108" ry="108"
        fill="var(--sticker-bg)" stroke="var(--frame)" stroke-width="5"/>

  <path class="headline-band" fill="var(--brand-blue)"
        d="M150,28 C195,20 230,40 265,48 C335,35 450,30 520,45 C600,30 690,33 728,45
           C800,30 900,26 965,40 C1012,56 1012,98 975,118 C930,136 850,132 728,134
           C705,130 692,122 670,134 C620,146 570,132 520,122 C450,140 330,146 245,114
           C200,126 130,136 104,104 C86,80 100,40 150,28 Z"/>

  <text class="sticker-text headline" x="113" y="100" textLength="855" lengthAdjust="spacingAndGlyphs">Stop starting, Start finishing</text>

  <text class="sticker-text tagline" x="245" y="228" textLength="822" lengthAdjust="spacingAndGlyphs">We show you how ...</text>

  <text class="sticker-text web-address" x="86" y="332" textLength="730" lengthAdjust="spacingAndGlyphs">www.quarvelon-beispiel.ch/kanban-coaching</text>

  <rect class="company-mark" x="878" y="306" width="62" height="62" fill="var(--brand-blue)"/>
  <text class="sticker-text company-name" x="952" y="346">Quarvelon ag</text>
</svg>
</body>
</html>
```